New Fresh design for online Rabbit Game

Hi,

we are a french company working on a online rabbits game for kids, and not kids.

Our website is www.trovelu.fr, but you can look at the US version : www.hoplark.com

We buy our actual design 2 years ago, but we now think it's too boring and washed out...

We need yours talent to make a really more exacting, more colorful, fresh and dynamic design.

In our game, players have to breed and train rabbits and to make them run races. Players run again friends or players.

Players are kids, between 8 and 15 years. But best players are often parents of these kids !

Our ambiance is clearly funny. We really like if color theme or background look like a nice blue sky, and / or beach. Something that make people happy to come, and say "You are here on holly days to have fun !"

I think the best is if we have 2 layouts, one for the Home page, and one for all other page.

For home page, we are really open to any proposition, we just need to keep our features :
- registration (with rabbit preview)
- connection
- game preview (images slide with small text)
- live race preview (as we have actually)

For other pages layout, we need a layout with a standard container (maybe 850 px width?), and our 2 navigation's bar.

We only need psd, no html integration.

Thanks for your help, please ask me for any questions.
Updates

Hi, 

I have just added some information, concerning layout.

Also we have just committed the budget.

Target Market(s)

Mostly kids between 8 and 15 years.

Industry/Entity Type

It Company

Requirements
Must have
• We already have some characters, like Mr Pebblo at the home page and our rabbits. We want to keep all of them, so new design have to match with there style (carton).

If you create an account, you will see we have a big nav bar with 6 tabs, and a little top bar. We absolutely need them to keep a easy navigation in website.

We also need some proposition of element style, like h1, h2, h3, hr, inputs, buttons, notification bubble, etc... So we can work to improve all our pages.
Nice to have
• I think the actual website is a little to wide (about 1000px width). Maybe something like 900px - 850px is more elegant ?
In this case, we can arrange pages to deal with it.

It can be cool if major colors are stil blue and green, to match a little with actual colors. But it's no very important.
Should not have
• We don't want too big header picture (for the all pages layout). I mean, players have to focus on the content.

We don't want photo realistic style, our style is cartoon.

We don't want flash. But Js animations are ok.

```html
<!DOCTYPE html>
<html lang="en">
<head>
<meta charset="utf-8">
<title>Burrowdash – The coolest racing and breeding game</title>
<link href="https://fonts.googleapis.com/css2?family=Ubuntu:wght@400;500;700&display=swap" rel="stylesheet">
<style>
:root{
  --sky-top:#14bfe6;
  --sky-bottom:#5fd6f0;
  --cloud:#8fe2f7;
  --grass:#a9c33b;
  --fence:#5a6b25;
  --panel:#ffffff;
  --teal:#1a8a9c;
  --teal-dark:#0f7486;
  --soft-blue:#e3f3f6;
  --tab-home:#5fdcf5;
  --tab-green:#b5dc3c;
  --tab-green-dark:#8fb82a;
  --red:#d40f14;
  --red-dark:#9c0a0e;
  --orange:#f08a00;
  --green-link:#6ea11a;
  --text:#333333;
  --white:#ffffff;
  --ring:#8fb82a;
}
*{box-sizing:border-box;margin:0;padding:0}
html,body{width:1200px;height:1100px;overflow:hidden}
body{font-family:"Ubuntu",sans-serif;color:var(--text);position:relative;
  background:linear-gradient(var(--sky-top) 0,var(--sky-bottom) 375px,var(--grass) 375px,var(--grass) 100%);}
.abs{position:absolute}
.cloud{position:absolute;background:var(--cloud);border-radius:40px}
.fence{position:absolute;top:343px;height:40px;background:linear-gradient(var(--fence) 0 5px,transparent 5px 26px,var(--fence) 26px 31px,transparent 31px);opacity:.85}
.fence-bunny{position:absolute;left:40px;top:310px;width:70px;height:65px;background:#e7e1d6;border-radius:30px}
.brand{position:absolute;left:0;width:1200px;top:58px;text-align:center;font-weight:500;font-size:56px;color:var(--white)}
.brand-dot{display:inline-block;width:18px;height:18px;border-radius:50%;background:var(--white);margin-right:12px;vertical-align:middle}
.tagline{position:absolute;left:0;width:1180px;top:146px;text-align:center;font-weight:700;font-size:21px;color:var(--white)}
.tab{position:absolute;top:192px;height:66px;border-radius:12px 12px 0 0;color:var(--white);font-weight:700;font-size:18px;text-align:center;padding-top:29px;background:var(--tab-green);text-shadow:0 1px 2px rgba(0,0,0,.3)}
.tab::before{content:"";position:absolute;left:50%;top:7px;width:14px;height:14px;margin-left:-7px;border-radius:50%;border:3px solid var(--tab-green-dark);background:var(--white)}
.tab--home{background:var(--tab-home)}
.tab--home::before{border-color:var(--teal-dark)}
.panel{position:absolute;left:147px;top:256px;width:898px;height:748px;background:var(--panel);border-radius:10px}
.mascot{position:absolute;left:880px;top:225px;width:190px;height:150px;border-radius:60px;background:linear-gradient(#7fbf2a,#d8e84a);border:4px solid var(--white)}
.signup{position:absolute;left:179px;top:296px;width:524px;height:253px;background:var(--soft-blue);border-radius:8px}
h2{font-weight:700;font-size:21px;color:var(--teal);text-transform:uppercase;line-height:1.05}
.promo{position:absolute;left:200px;top:16px;width:308px;text-align:right;color:var(--red);font-size:17.5px}
.step{position:absolute;font-size:16px;display:flex;align-items:center;gap:6px}
.step-num{width:38px;height:38px;border-radius:50%;border:3px solid var(--ring);background:var(--white);color:var(--ring);font-size:19px;display:flex;align-items:center;justify-content:center}
.bunny-name{position:absolute;left:23px;top:96px;color:var(--teal);font-size:15px}
.picker{position:absolute;left:21px;width:127px;height:32px;border:1px solid #9bd0dc;border-radius:5px;background:linear-gradient(#fff,#eef8fa);color:var(--teal);font-size:15px;display:flex;align-items:center;justify-content:space-between;padding:0 8px}
.picker svg{width:10px;height:14px}
.preview-bunny{position:absolute;left:158px;top:165px;width:66px;height:64px;background:#e6e0d4;border-radius:30px}
.vdivider{position:absolute;left:244px;top:55px;height:172px;border-left:1px dashed #9bbfc6}
.hdivider{position:absolute;left:262px;top:135px;width:246px;border-top:1px dashed #9bbfc6}
.field{position:absolute;height:33px;border:1px solid #b8c4c8;border-radius:5px;background:var(--white)}
.btn-play{position:absolute;width:112px;height:38px}
.btn-play span{position:absolute;left:0;top:0;width:100px;height:38px;line-height:36px;text-align:center;font-weight:700;font-size:21px;color:var(--white)}
.label{position:absolute;font-size:16px}
.help{position:absolute;left:932px;top:443px;width:24px;height:20px}
.forgot{position:absolute;left:875px;top:488px;font-size:14px;line-height:1.3;color:#444}
.dash{position:absolute;left:178px;top:585px;width:840px;border-top:1px dashed #aaa}
.subnav{position:absolute;left:181px;top:639px;font-size:14.5px;color:var(--green-link)}
.subnav .current{color:var(--orange)}
.subnav i{font-style:normal;color:#888;margin:0 8px}
.card{position:absolute;top:672px;height:292px;border-radius:6px;background:var(--white);box-shadow:0 0 0 3px #e8f2c0,0 2px 6px rgba(0,0,0,.15)}
.shot{position:absolute;border-radius:4px}
.caption-left{position:absolute;left:183px;top:900px;width:389px;height:56px;background:rgba(110,160,30,.92);color:var(--white);font-size:14px;line-height:1.35;padding:6px 6px}
.caption-right{position:absolute;left:619px;top:888px;width:389px;height:68px;background:#1fb2cf;color:var(--white);font-weight:700;font-size:22px;line-height:1.1;text-align:center;padding-top:11px}
.footer{position:absolute;left:147px;top:1037px;font-size:14px;color:var(--white)}
.partners{position:absolute;left:883px;top:1037px;font-size:14px;color:var(--white)}
.badge{position:absolute;left:958px;top:1031px;width:88px;height:31px;background:#1b3d8f;border:1px solid #0c1f4d}
</style>
</head>
<body>
  <div class="cloud" role="img" aria-label="Cloud" style="left:335px;top:25px;width:102px;height:55px"></div>
  <div class="cloud" role="img" aria-label="Cloud" style="left:117px;top:88px;width:105px;height:78px"></div>
  <div class="cloud" role="img" aria-label="Cloud" style="left:798px;top:32px;width:130px;height:82px"></div>
  <div class="cloud" role="img" aria-label="Cloud" style="left:1073px;top:10px;width:102px;height:52px"></div>
  <div class="fence" role="img" aria-label="Wooden fence" style="left:0;width:150px"></div>
  <div class="fence" role="img" aria-label="Wooden fence" style="left:1045px;width:155px"></div>
  <div class="fence-bunny" role="img" aria-label="Cartoon bunny peeking over the fence"></div>

  <div class="brand"><span class="brand-dot"></span>Burrowdash</div>
  <div class="tagline">THE COOLEST RACING AND BREEDING GAME</div>

  <nav>
    <div class="tab tab--home" style="left:313px;width:124px">HOME</div>
    <div class="tab" style="left:453px;width:129px">NEWS</div>
    <div class="tab" style="left:598px;width:130px">FORUM</div>
    <div class="tab" style="left:744px;width:136px">RECORDS</div>
  </nav>

  <main class="panel"></main>
  <div class="mascot" role="img" aria-label="Mr Pebblo, the cartoon turtle coach with a cap and stopwatch"></div>

  <section class="signup">
    <h2 class="abs" style="left:19px;top:17px">New Player</h2>
    <div class="promo">Register in just a Couple of Seconds</div>
    <div class="step" style="left:17px;top:50px"><span class="step-num">1</span>Choose your Bunny</div>
    <div class="bunny-name">POMPON</div>
    <div class="picker" style="top:122px"><svg viewBox="0 0 10 14"><path d="M8 1 2 7l6 6" fill="none" stroke="currentColor" stroke-width="2.5"/></svg>Original<svg viewBox="0 0 10 14"><path d="m2 1 6 6-6 6" fill="none" stroke="currentColor" stroke-width="2.5"/></svg></div>
    <div class="picker" style="top:159px"><svg viewBox="0 0 10 14"><path d="M8 1 2 7l6 6" fill="none" stroke="currentColor" stroke-width="2.5"/></svg>Gray<svg viewBox="0 0 10 14"><path d="m2 1 6 6-6 6" fill="none" stroke="currentColor" stroke-width="2.5"/></svg></div>
    <div class="picker" style="top:196px"><svg viewBox="0 0 10 14"><path d="M8 1 2 7l6 6" fill="none" stroke="currentColor" stroke-width="2.5"/></svg>Male<svg viewBox="0 0 10 14"><path d="m2 1 6 6-6 6" fill="none" stroke="currentColor" stroke-width="2.5"/></svg></div>
    <div class="preview-bunny" role="img" aria-label="Preview of the chosen bunny"></div>
    <div class="vdivider"></div>
    <div class="step" style="left:268px;top:50px"><span class="step-num">2</span>Choose a Username</div>
    <div class="field" style="left:315px;top:89px;width:146px;height:31px;border-color:#d6e6ea"></div>
    <div class="hdivider"></div>
    <div class="step" style="left:268px;top:147px"><span class="step-num">3</span>OK! We are good to go!</div>
    <div class="btn-play" style="left:316px;top:186px">
      <svg width="112" height="38" viewBox="0 0 112 38"><path d="M0 0h96l16 19-16 19H0z" fill="var(--red-dark)"/><path d="M0 0h94l14 17-14 17H0z" fill="var(--red)"/></svg>
      <span>PLAY</span>
    </div>
  </section>

  <section>
    <h2 class="abs" style="left:738px;top:311px">Connexion</h2>
    <div class="label" style="left:742px;top:346px">Username</div>
    <div class="field" style="left:744px;top:370px;width:177px"></div>
    <div class="label" style="left:742px;top:413px">Password</div>
    <div class="field" style="left:744px;top:437px;width:177px"></div>
    <svg class="help" viewBox="0 0 24 20"><path d="M12 1C6 1 1 4.5 1 9c0 3 2 5 5 6.5L4 19l6-3h2c6 0 11-3.5 11-7.5S18 1 12 1z" fill="#fff" stroke="#222" stroke-width="1.4"/><text x="12" y="13" text-anchor="middle" font-size="11" font-weight="700" font-family="Ubuntu,sans-serif">?</text></svg>
    <div class="btn-play" style="left:746px;top:486px;width:112px">
      <svg width="112" height="38" viewBox="0 0 112 38"><path d="M0 0h96l16 19-16 19H0z" fill="var(--red-dark)"/><path d="M0 0h94l14 17-14 17H0z" fill="var(--red)"/></svg>
      <span>PLAY</span>
    </div>
    <div class="forgot">Forgotten your<br>Password?</div>
  </section>

  <div class="dash"></div>

  <section>
    <h2 class="abs" style="left:180px;top:608px">Game Overview</h2>
    <div class="subnav"><span class="current">Your Pen</span><i>|</i>Your Allotment<i>|</i>Professions<i>|</i>Universe</div>
    <div class="card" style="left:178px;width:400px"></div>
    <div class="shot" role="img" aria-label="Game view of a grassy pen where bunnies play, with a training panel below" style="left:183px;top:678px;width:389px;height:278px;background:linear-gradient(#3fa83a,#2f9330 75%,#c5d88a 75%)"></div>
    <div class="caption-left">Breed, educate and train your bunnies in your pen. Watch as they play and grow up together <b>under your very eyes!</b></div>
  </section>

  <section>
    <h2 class="abs" style="left:616px;top:608px">Take part in races with<br>other players</h2>
    <div class="card" style="left:612px;width:402px"></div>
    <div class="shot" role="img" aria-label="Live race scene with bunnies running on dirt lanes in front of spectators" style="left:619px;top:678px;width:389px;height:278px;background:linear-gradient(#8a5a2a 0,#8a5a2a 38px,#9aa1b0 38px,#9aa1b0 98px,#b07430 98px)"></div>
    <div class="caption-right">Come and Train your Bunnies<br>and Challenge your Friends</div>
  </section>

  <footer>
    <div class="footer">Rules - General Terms and Conditions - Contact - Burrowdash.com 3.0</div>
    <div class="partners">Partners:</div>
    <div class="badge" role="img" aria-label="Partner listing badge"></div>
  </footer>
</body>
</html>
```